Feral Horizon, a 3d voxel survival video game needs a card for gaming conventions

I am the lead developer for Feral Horizon http://www.FeralHorizon.example and need a business card to hand out at an indie gaming convention
The card would need to include the game name, website url, my name, position (Lead Developer), e-mail and phone number
The game is a 3d, voxel (with smooth terrain) based survival game with guns and wildlife. The main icon of the game would likely be a grizzly bear but I am willing to accept other designs too.
Attached is a media kit for the game with some images you can use but don't have to its just what little art I can provide. Anything on the website or from the video game can also be used. unrelated art can also be used.
Target Market(s)
Indie Developers/publishers at conferences
Industry/Entity Type
Games
Contact Information for Business Card
Name: Corwin Aldersby
Position: Lead Developer
E-mail: Pale_Lanterns@mailbox.example
Phone number: 555-207-3186

```html
<!DOCTYPE html>
<html lang="en">
<head>
<meta charset="utf-8">
<title>Feral Horizon — Business Card</title>
<link rel="stylesheet" href="https://fonts.googleapis.com/css2?family=Open+Sans:ital,wght@0,400;0,700;0,800;1,400&family=Patrick+Hand+SC&display=swap">
<style>
  :root {
    --page-bg: #ffffff;
    --front-light: #b4aa8a;
    --front-mid: #8f8668;
    --front-dark: #4a4634;
    --back-brown: #3e1a0e;
    --back-white: #ffffff;
    --logo-red: #8e2a1c;
    --text-light: #ffffff;
    --bear-light: #8a5a34;
    --bear-dark: #3a2313;
    --card-shadow: rgba(0, 0, 0, 0.28);
  }
  * { margin: 0; padding: 0; box-sizing: border-box; }
  html, body {
    width: 1200px;
    height: 1200px;
    overflow: hidden;
    background: var(--page-bg);
  }
  .canvas {
    position: relative;
    width: 1200px;
    height: 1200px;
  }
  .card {
    position: absolute;
    border-radius: 26px;
    overflow: hidden;
    box-shadow: 0 8px 22px var(--card-shadow);
  }

  /* Front face */
  .card-front {
    left: 201px;
    top: 77px;
    width: 798px;
    height: 456px;
    background: radial-gradient(ellipse 70% 75% at 68% 68%, var(--front-light) 0%, var(--front-mid) 55%, var(--front-dark) 100%);
  }
  .front-bear {
    position: absolute;
    left: 495px;
    top: 47px;
    width: 280px;
    height: 268px;
    border-radius: 46% 40% 12% 30%;
    background: radial-gradient(ellipse at 40% 35%, var(--bear-light) 0%, var(--bear-dark) 70%, rgba(58, 35, 19, 0) 100%);
  }
  .front-wordmark {
    position: absolute;
    left: 70px;
    top: 170px;
    width: 560px;
    font-family: "Open Sans", sans-serif;
    font-weight: 800;
    font-size: 66px;
    line-height: 1.05;
    letter-spacing: 2px;
    color: var(--logo-red);
    text-align: center;
    text-transform: uppercase;
  }

  /* Back face */
  .card-back {
    left: 201px;
    top: 600px;
    width: 809px;
    height: 462px;
    background: var(--back-white);
  }
  .back-band {
    position: absolute;
    left: 0;
    top: 0;
    width: 100%;
    height: 318px;
    background: var(--back-brown);
  }
  .holder-name {
    position: absolute;
    left: 85px;
    top: 30px;
    font-family: "Patrick Hand SC", cursive;
    font-size: 44px;
    line-height: 1;
    color: var(--text-light);
    letter-spacing: 0.5px;
  }
  .holder-role {
    position: absolute;
    left: 86px;
    top: 76px;
    font-family: "Open Sans", sans-serif;
    font-style: italic;
    font-size: 25px;
    color: var(--text-light);
  }
  .back-bear {
    position: absolute;
    left: 127px;
    top: 128px;
    width: 162px;
    height: 156px;
    border-radius: 48% 52% 14% 14%;
    background: radial-gradient(ellipse at 55% 35%, var(--bear-light) 0%, var(--bear-dark) 72%, rgba(58, 35, 19, 0) 100%);
  }
  .contact-list {
    position: absolute;
    left: 410px;
    top: 170px;
    list-style: none;
  }
  .contact-item {
    display: flex;
    align-items: center;
    height: 32px;
    font-family: "Open Sans", sans-serif;
    font-size: 21px;
    color: var(--text-light);
  }
  .contact-icon {
    width: 18px;
    height: 18px;
    margin-right: 32px;
    flex: none;
  }
  .back-wordmark {
    position: absolute;
    left: 0;
    top: 350px;
    width: 100%;
    text-align: center;
    font-family: "Open Sans", sans-serif;
    font-weight: 800;
    font-size: 58px;
    line-height: 1;
    letter-spacing: 3px;
    color: var(--logo-red);
    text-transform: uppercase;
  }
</style>
</head>
<body>
<main class="canvas">

  <section class="card card-front">
    <div class="front-bear" role="img" aria-label="Photograph of a roaring grizzly bear"></div>
    <div class="front-wordmark">Feral<br>Horizon</div>
  </section>

  <section class="card card-back">
    <div class="back-band">
      <div class="holder-name">CORWIN ALDERSBY</div>
      <div class="holder-role">Leader Developer</div>
      <div class="back-bear" role="img" aria-label="Photograph of a roaring grizzly bear"></div>
      <ul class="contact-list">
        <li class="contact-item">
          <svg class="contact-icon" viewBox="0 0 18 18" aria-hidden="true">
            <circle cx="9" cy="9" r="9" fill="#ffffff"/>
            <path d="M4.5 9 L9 5 L13.5 9 M6 8.2 V12.8 H12 V8.2" fill="none" stroke="#3e1a0e" stroke-width="1.6" stroke-linejoin="round"/>
          </svg>
          www.FeralHorizon.example
        </li>
        <li class="contact-item">
          <svg class="contact-icon" viewBox="0 0 18 18" aria-hidden="true">
            <circle cx="9" cy="9" r="9" fill="#ffffff"/>
            <rect x="4.5" y="6" width="9" height="6.4" fill="#3e1a0e"/>
            <path d="M4.5 6 L9 9.6 L13.5 6" fill="none" stroke="#ffffff" stroke-width="1"/>
          </svg>
          Pale_Lanterns@mailbox.example
        </li>
        <li class="contact-item">
          <svg class="contact-icon" viewBox="0 0 18 18" aria-hidden="true">
            <circle cx="9" cy="9" r="9" fill="#ffffff"/>
            <rect x="6.3" y="4.3" width="5.4" height="9.4" rx="1" fill="#3e1a0e"/>
            <rect x="7.3" y="5.6" width="3.4" height="5.6" fill="#ffffff"/>
          </svg>
          555-207-3186
        </li>
      </ul>
    </div>
    <div class="back-wordmark">Feral Horizon</div>
  </section>

</main>
</body>
</html>
```